missions focus sunday

i am a christian who is tasked to do a simple presentation of missions work in northern germany. i have some ideas which i have sketched out as enclosed.
can you do the postcard in black background with words/diagrams in white? thanks

Industry/Entity Type

Christian

```html
<!DOCTYPE html>
<html lang="en">
<head>
<meta charset="utf-8">
<title>Missions Focus Sunday – Front Postcard</title>
<link href="https://fonts.googleapis.com/css2?family=Architects+Daughter&family=Open+Sans:wght@400&display=swap" rel="stylesheet">
<style>
  :root {
    --paper: #ffffff;
    --board-centre: #3b3b3c;
    --board-edge: #1e1d1e;
    --chalk: #ffffff;
    --ink: #1e1d1e;
    --flag-black: #000000;
    --flag-red: #ea2d2b;
    --flag-gold: #f9e62f;
    --sg-red: #df1f26;
    --caption: #7a7a7a;
  }
  * { margin: 0; padding: 0; box-sizing: border-box; }
  html, body {
    width: 1200px; height: 1000px; overflow: hidden;
    background: var(--paper);
  }
  .sheet { position: relative; width: 1200px; height: 1000px; }
  .postcard {
    position: absolute; left: 36px; top: 27px; width: 1123px; height: 870px;
    background: radial-gradient(ellipse at 48% 50%, var(--board-centre) 0%, #2c2b2c 45%, var(--board-edge) 100%);
    overflow: hidden;
  }
  .artwork { position: absolute; inset: 0; }
  .chalk-text {
    position: absolute;
    font-family: "Architects Daughter", cursive;
    font-weight: 400;
    color: var(--chalk);
    text-transform: uppercase;
    letter-spacing: 3px;
    line-height: 37px;
    white-space: nowrap;
  }
  .tagline-power { left: 72px; top: 80px; font-size: 29px; }
  .tagline-power sup { font-size: 17px; vertical-align: 10px; letter-spacing: 0; }
  .tagline-call {
    left: 770px; top: 662px; width: 292px;
    font-size: 29px; text-align: right;
  }
  .dream-text {
    left: 300px; top: 370px; width: 460px;
    font-size: 36px; color: var(--ink); text-align: center; line-height: 54px;
    text-shadow: 0 6px 8px rgba(0,0,0,0.25);
  }
  .cloud { filter: drop-shadow(0 14px 18px rgba(0,0,0,0.55)); }
  .flag { filter: drop-shadow(0 10px 14px rgba(0,0,0,0.6)); }
  .airplane { filter: drop-shadow(0 8px 10px rgba(0,0,0,0.5)); }
  .caption {
    position: absolute; right: 41px; top: 919px;
    font-family: "Open Sans", sans-serif; font-size: 21px;
    color: var(--caption); letter-spacing: 0.5px;
  }
</style>
</head>
<body>
<div class="sheet">
  <section class="postcard">
    <svg class="artwork" width="1123" height="870" viewBox="36 27 1123 870" xmlns="http://www.w3.org/2000/svg">
      <defs>
        <clipPath id="flag-germany-shape"><rect x="877" y="85" width="185" height="123" rx="24"/></clipPath>
        <clipPath id="flag-singapore-shape"><rect x="103" y="666" width="182" height="124" rx="24"/></clipPath>
        <polygon id="star" points="0,-6 1.8,-1.9 6,-1.9 2.6,0.9 3.7,5 0,2.5 -3.7,5 -2.6,0.9 -6,-1.9 -1.8,-1.9"/>
      </defs>

      <!-- journey arrows -->
      <g class="journey-arrows" fill="none" stroke="var(--chalk)" stroke-width="3.5" stroke-linecap="round">
        <path d="M140 645 C 150 420, 240 230, 470 160 C 620 118, 760 118, 850 120"/>
        <path d="M843 113 L856 120 L843 127"/>
        <path d="M1007 225 C 1000 420, 900 640, 640 720 C 520 752, 400 758, 308 758"/>
        <path d="M318 751 L305 758 L318 765"/>
      </g>

      <!-- footsteps -->
      <rect role="img" aria-label="Two white footprints" x="236" y="104" width="158" height="132" rx="40" fill="#d8d8d8" opacity="0.85"/>

      <!-- airplane -->
      <g class="airplane" fill="var(--chalk)" transform="translate(772 770) rotate(-30) scale(0.85)">
        <path d="M-78 -7 L56 -7 Q80 0 56 7 L-78 7 Z"/>
        <path d="M12 -7 L-14 -62 L-30 -62 L-16 -7 Z"/>
        <path d="M12 7 L-14 62 L-30 62 L-16 7 Z"/>
        <path d="M-58 -7 L-72 -30 L-82 -30 L-76 -7 Z"/>
        <path d="M-58 7 L-72 30 L-82 30 L-76 7 Z"/>
      </g>

      <!-- dream cloud -->
      <path class="cloud" fill="var(--chalk)"
        d="M392 556 C 345 556 322 515 328 472 C 334 425 365 398 400 394
           C 392 332 432 276 492 262 C 552 250 602 280 626 322
           C 668 300 722 326 736 374 C 790 378 820 422 812 472
           C 806 522 780 556 740 558 Z"/>

      <!-- Germany flag -->
      <g class="flag flag-germany">
        <g clip-path="url(#flag-germany-shape)">
          <rect x="877" y="85" width="185" height="41" fill="var(--flag-black)"/>
          <rect x="877" y="126" width="185" height="41" fill="var(--flag-red)"/>
          <rect x="877" y="167" width="185" height="41" fill="var(--flag-gold)"/>
        </g>
        <rect x="877" y="85" width="185" height="123" rx="24" fill="none" stroke="var(--chalk)" stroke-width="4"/>
      </g>

      <!-- Singapore flag -->
      <g class="flag flag-singapore">
        <g clip-path="url(#flag-singapore-shape)">
          <rect x="103" y="666" width="182" height="62" fill="var(--sg-red)"/>
          <rect x="103" y="728" width="182" height="62" fill="var(--chalk)"/>
          <circle cx="135" cy="697" r="20" fill="var(--chalk)"/>
          <circle cx="144" cy="697" r="19" fill="var(--sg-red)"/>
          <g fill="var(--chalk)">
            <use href="#star" x="151" y="686"/>
            <use href="#star" x="162" y="694"/>
            <use href="#star" x="158" y="708"/>
            <use href="#star" x="144" y="708"/>
            <use href="#star" x="140" y="694"/>
          </g>
        </g>
        <rect x="103" y="666" width="182" height="124" rx="24" fill="none" stroke="var(--chalk)" stroke-width="4"/>
      </g>
    </svg>

    <p class="chalk-text tagline-power">The<br>Power<br>of 2<sup>oo</sup></p>
    <p class="chalk-text dream-text">Last night<br>dream of this</p>
    <p class="chalk-text tagline-call">Answering the<br>“Come” call</p>
  </section>
  <p class="caption">FRONT POSTCARD</p>
</div>
</body>
</html>
```